Qorvel Consulting

We focus on Data Recovery but we also do Network Security. We recover data from all types of hard drive form factors 3.5", 2.5", 1", 1.8", 5.25", 8" with any kind of interface IDE(PATA), SATA, mSATA, SCSI, SAS and Fibre Channel. All RAID Arrays 0, 1, 2, 3, 4, 5, 10 including nested levels like RAID 0+1, 1+0, 100, 0+3, 50 and 60, flash drives, like tablets, cellphones, usb drives, memory cards(SD, miniSD, Data Wafer(tavik))

Actually you can gather any information or text from any data recovery site, cause is usually the same info, we would probably change a couple of things from the description so it wont look the same. One thing though, we want to make clear to users not to attempt data recovery themselves and to ship the faulty device to us, maybe we can illustrate this?

the Data Recovery link can have sub menus like "Data Recovery Process - Data Recovery Services - F.A.Q"

the Penetration Testing can have sub menus like "F.A.Q - Pentest Process - Pentest Services"

Here are links from website so you gather information:

-http://www.mydiskwentdark.example/

-http://www.bitrescuelabsrecovery.example/

-http://www.pulvenbytes.example/

http://fetchlostfiles.example/lp/hard-drive-recovery.aspx?src=Brovix&gclid=ZTRWq4XplnQMDA-kwPbcf7HE2s
http://www.qulm.example/
http://www.venbrisfield.example/data-recovery/
http://www.tzwdatarecovery.example/

thanks.

Target Market(s)

Any PC user

Industry/Entity Type

Data Recovery

Requirements
Must have
• - Language and geographic navigation
- Home page navigation
- Global navigation
- Breadcrumbs
Nice to have
• - Sliders
-Drop down navigation

```html
<!DOCTYPE html>
<html lang="en">
<head>
<meta charset="utf-8">
<title>Qorvel Consulting</title>
<link rel="stylesheet" href="https://fonts.googleapis.com/css2?family=Roboto+Condensed:wght@300;400&family=Open+Sans:wght@400;600&family=Lato:wght@400;700&family=Kalam:wght@300&family=Noto+Serif&display=swap">
<style>
:root{
  --red:#ee1c1c;
  --ink:#2a2a2a;
  --muted:#7a7a7a;
  --side:#dedede;
  --paper:#ffffff;
  --footer:#ececec;
  --band:#e4e4e4;
  --slide:#5a4a3a;
}
*{margin:0;padding:0;box-sizing:border-box}
html,body{width:1200px;height:1000px;overflow:hidden}
body{background:var(--side);position:relative;font-family:'Open Sans',sans-serif;color:var(--ink)}
.page{position:absolute;left:90px;top:0;width:1018px;height:785px;background:var(--paper)}
.site-footer{position:absolute;left:90px;top:785px;width:1018px;height:215px;background:var(--footer)}
.abs{position:absolute}

.brand{left:207px;top:38px;display:flex;align-items:center;gap:8px}
.brand-name{font-family:'Open Sans',sans-serif;font-weight:600;font-size:40px;color:var(--ink);letter-spacing:-1px;line-height:1}
.brand-mark{width:12px;height:12px;background:var(--red)}

.main-nav{right:207px;top:58px;display:flex;font-family:'Roboto Condensed',sans-serif;font-weight:300;font-size:17px;letter-spacing:.3px}
.main-nav a{color:var(--ink);text-decoration:none;padding:0 10px;border-right:1px solid var(--ink);line-height:19px}
.main-nav a.active{color:var(--red)}

.tagline{left:207px;top:136px;width:786px;text-align:center;font-family:'Kalam',cursive;font-weight:300;font-size:16px;line-height:32px;color:#333}

.slider{left:207px;top:218px;width:786px;height:270px;background:linear-gradient(120deg,#3a3a3a 0%,#7a6a50 35%,#4a4038 60%,#8a5a3a 85%,#3a3430 100%)}
.slide-caption{left:207px;top:428px;width:786px;height:60px;background:rgba(30,30,30,.75)}
.slide-caption .title{position:absolute;left:19px;top:14px;font-family:'Roboto Condensed',sans-serif;font-size:23px;color:#fff}
.slide-caption .more{position:absolute;left:638px;top:21px;font-family:'Open Sans',sans-serif;font-weight:600;font-size:13px;color:var(--red);text-transform:uppercase}
.slide-arrow{left:993px;width:32px;height:29px;background:#e8e8e8;display:flex;align-items:center;justify-content:center}
.slide-progress{left:207px;top:488px;width:786px;height:5px;background:#9a9a9a}
.slide-progress span{display:block;width:260px;height:5px;background:var(--red)}

.about-title{left:208px;top:524px;font-family:'Roboto Condensed',sans-serif;font-weight:300;font-size:33px}
.about-text{left:206px;top:579px;width:290px;font-size:13.5px;line-height:15.5px;color:#111}
.learn-more{left:405px;top:659px;font-family:'Lato',sans-serif;font-weight:700;font-size:11px;color:var(--red);text-decoration:none}

.service-card{top:531px;width:142px;height:158px;border-top:3px solid var(--red);border-bottom:2px solid var(--ink);background:var(--band)}
.service-card .visual{height:115px}
.service-card .label{height:38px;display:flex;align-items:center;justify-content:center;font-size:13.5px;color:#111}

.news-bar{left:207px;top:725px;width:786px;height:34px;background:var(--band)}
.news-bar .dot{position:absolute;left:15px;top:10px;width:14px;height:14px;border-radius:50%;background:#555}
.news-bar .text{position:absolute;left:53px;top:8px;font-family:'Noto Serif',serif;font-size:13px;color:#222}
.news-bar .text a{color:var(--red);text-decoration:none}
.news-bar .tag{position:absolute;right:0;top:0;width:128px;height:34px;background:var(--red);clip-path:polygon(0 50%,8% 0,100% 0,100% 100%,8% 100%);color:#fff;font-family:'Lato',sans-serif;font-weight:700;font-size:12px;display:flex;align-items:center;justify-content:center;padding-left:8px}

.footer-col h4{font-family:'Lato',sans-serif;font-weight:700;font-size:10.5px;color:#333;margin-bottom:17px}
.footer-col p{font-size:13px;line-height:21.8px;color:var(--muted);letter-spacing:.2px}
.footer-col p a{color:var(--red);text-decoration:none}
.copyright{left:234px;top:962px;font-size:13px;color:#333}
.social{left:749px;top:964px;display:flex;align-items:center;gap:14px;font-family:'Lato',sans-serif;font-size:11px;color:#333}
.social .label{color:#555}
.social span.item{display:flex;align-items:center;gap:5px}
.social i{display:inline-block;width:12px;height:12px;background:#333}
.social-rule{left:749px;top:995px;width:271px;height:1px;background:#c8c8c8}
</style>
</head>
<body>
<div class="page"></div>

<header>
  <div class="abs brand"><span class="brand-name">qorvel</span><span class="brand-mark"></span></div>
  <nav class="abs main-nav">
    <a class="active" href="#">HOME</a>
    <a href="#">DATA RECOVERY</a>
    <a href="#">INFORMATION SECURITY</a>
    <a href="#">CONTACT</a>
  </nav>
</header>

<p class="abs tagline">Qorvel Consulting provides immediate response consultations to organizations requiring critical case<br>attention or security requirements or a need to perform a certain types of on site data recovery.</p>

<section>
  <div class="abs slider" role="img" aria-label="Close-up of an opened hard drive platter overlaid with glowing binary digits"></div>
  <div class="abs slide-caption">
    <span class="title">Data recovery solutions for valuable digitally stored information</span>
    <span class="more">Find out more »</span>
  </div>
  <div class="abs slide-arrow" style="top:428px"><svg width="10" height="14" viewBox="0 0 10 14"><path d="M2 1l6 6-6 6" fill="none" stroke="#555" stroke-width="1.3"/></svg></div>
  <div class="abs slide-arrow" style="top:459px"><svg width="10" height="14" viewBox="0 0 10 14"><path d="M8 1L2 7l6 6" fill="none" stroke="#555" stroke-width="1.3"/></svg></div>
  <div class="abs slide-progress"><span></span></div>
</section>

<section>
  <h2 class="abs about-title">About Qorvel</h2>
  <p class="abs about-text">Provides data recovery training, consulting and service provider. In the past 10 years we have developed knowhow methods and technology.</p>
  <a class="abs learn-more" href="#">LEARN MORE <svg width="7" height="9" viewBox="0 0 7 9"><path d="M1.5 1l3.5 3.5L1.5 8" fill="none" stroke="#ee1c1c" stroke-width="2"/></svg></a>

  <div class="abs service-card" style="left:528px">
    <div class="visual" role="img" aria-label="Pink and purple capsule pill on a pale background" style="background:linear-gradient(180deg,#eef0f4,#e3e6ec)"></div>
    <div class="label">Data Recovery</div>
  </div>
  <div class="abs service-card" style="left:689px">
    <div class="visual" role="img" aria-label="Silver key lying on a scratched grey-green surface" style="background:radial-gradient(circle at 50% 50%,#8a9088,#555c55)"></div>
    <div class="label">Information Security</div>
  </div>
  <div class="abs service-card" style="left:850px">
    <div class="visual" role="img" aria-label="Pencil tied in a knot on a grey background" style="background:linear-gradient(180deg,#8a8a8a,#6e6e6e)"></div>
    <div class="label">Penetration Testing</div>
  </div>
</section>

<div class="abs news-bar">
  <span class="dot"></span>
  <span class="text">How to recover deleted data? <a href="#">http://qv.example/p4k-7h</a></span>
  <span class="tag">LATEST NEWS</span>
</div>

<footer class="site-footer"></footer>
<svg class="abs" style="left:197px;top:812px" width="24" height="36" viewBox="0 0 24 36"><path d="M12 1C6 1 1 5.8 1 12c0 8 11 23 11 23s11-15 11-23C23 5.8 18 1 12 1z" fill="#ee1c1c"/><circle cx="12" cy="12" r="4.5" fill="#ececec"/></svg>
<div class="abs footer-col" style="left:234px;top:818px">
  <h4>CONTACT US AT:</h4>
  <p>Linden str. 27<br>10021 NY, NY<br>Email: <a href="#">mailbox@qorvel.example</a></p>
</div>
<div class="abs footer-col" style="left:496px;top:818px">
  <h4>ABOUT US:</h4>
  <p>Our History<br>Our Clients<br>Partners<br>Meet the Team</p>
</div>
<div class="abs footer-col" style="left:631px;top:818px">
  <h4>SERVICES:</h4>
  <p>Data recovery<br>Information Security<br>Penetration Testing<br>Trainings and Seminars</p>
</div>
<p class="abs copyright">© 2013 — Qorvel Consulting</p>
<div class="abs social">
  <span class="label">Follow us on:</span>
  <span class="item"><i></i>Friendly</span>
  <span class="item"><i style="border-radius:50%"></i>Chirper</span>
  <span class="item"><svg width="12" height="12" viewBox="0 0 12 12"><circle cx="2" cy="10" r="1.6" fill="#333"/><path d="M1 5.5a5.5 5.5 0 0 1 5.5 5.5M1 1.5A9.5 9.5 0 0 1 10.5 11" fill="none" stroke="#333" stroke-width="1.8"/></svg>RSS</span>
</div>
<div class="abs social-rule"></div>
</body>
</html>
```